Ledgerwise Forge - WordPress Theme & Logo

Design a logo and Wordpress website design for Ledgerwise Forge. Ledgerwise Forge provides cryptocurrency development services to clients who need a team to create & continue developing a new cryptocurrency or who want to replace their current cryptocurrency development team. more details in the attached document.
Updates

Target Market(s)

Entrepreneurs who are building a business / platform that makes use of an underlying cryptocurrency.

Logo Text

LF or Ledgerwise Forge

Coding

Coded - Design and coding required

Font styles to use
Sans Serif

Requirements
Must have
• Professional logo, complete coded Wordpress theme for all pages, containing all specified links and buttons
Nice to have
• It would be nice if the buttons that are meant to integrate with Dealstream contain the necessary code for that. I can provide any necessary Dealstream details from my account.
Should not have
• Slow loading time

```html
<!DOCTYPE html>
<html lang="en">
<head>
<meta charset="utf-8">
<title>Ledgerwise Forge – Cryptocurrency Development</title>
<link href="https://fonts.googleapis.com/css2?family=Poppins:wght@500;600;700&family=Roboto:wght@400;500&display=swap" rel="stylesheet">
<style>
:root{
  --navy:#0b0f4a;
  --navy-deep:#070a35;
  --blue:#1c3fd6;
  --sky:#2f7df0;
  --teal:#15b39a;
  --green:#1fd39b;
  --ink:#111111;
  --text:#3a3a3a;
  --pale:#e8f2fd;
  --pale-blue:#c4dcfb;
  --pale-green:#c3f1e2;
  --footer:#141414;
  --white:#ffffff;
}
*{margin:0;padding:0;box-sizing:border-box}
html,body{width:1200px;height:3476px;overflow:hidden;background:var(--white)}
body{position:relative;font-family:'Roboto',Arial,sans-serif;color:var(--text)}
a{text-decoration:none}
.abs{position:absolute}
h1,h2,h3,.brand{font-family:'Poppins',Arial,sans-serif;color:var(--ink)}
.btn{position:absolute;display:flex;align-items:center;justify-content:center;border-radius:30px;color:var(--white);font-family:'Poppins',Arial,sans-serif;font-weight:600;font-size:15px;background:linear-gradient(90deg,var(--teal),var(--blue));text-decoration:none}
/* hero */
.hero-bg{position:absolute;left:0;top:0;width:1200px;height:780px}
.nav a{position:absolute;top:46px;color:var(--white);font-family:'Roboto',Arial,sans-serif;font-weight:500;font-size:15px;text-decoration:none;letter-spacing:.2px}
.brand-mark{position:absolute;display:flex;align-items:center;gap:10px;color:var(--white);font-weight:700}
.brand-mark .dot{border-radius:50%;background:var(--white)}
.flag{position:absolute;left:761px;top:48px;width:34px;height:18px;background:linear-gradient(180deg,#1a3a9c 0 40%,#d7263d 40% 60%,#1a3a9c 60%);border:1px solid #fff}
.btn-outline{position:absolute;left:824px;top:28px;width:275px;height:54px;border:2px solid var(--white);border-radius:30px;color:var(--white);display:flex;align-items:center;justify-content:center;font-family:'Poppins',Arial,sans-serif;font-weight:600;font-size:15px;text-decoration:none}
.hero-title{position:absolute;left:101px;top:144px;color:var(--white);font-size:36px;line-height:43px;font-weight:700;letter-spacing:-0.5px;white-space:nowrap}
.hero-copy{position:absolute;left:101px;top:288px;width:470px;color:var(--white);font-size:14px;line-height:27px}
.hero-art{position:absolute;left:580px;top:160px;width:515px;height:470px;border-radius:40px;background:radial-gradient(circle at 50% 45%,#1fd39b 0 14%,#2c49d8 34%,rgba(28,40,150,.4) 62%,rgba(11,15,74,0) 75%)}
/* why */
.center{position:absolute;left:0;width:1200px;text-align:center}
.why-title{top:820px;font-size:38px;font-weight:700}
.feature{position:absolute;top:910px;width:300px;text-align:center}
.feature svg{display:block;margin:0 auto 10px}
.feature h3{font-size:26px;font-weight:700;line-height:40px}
.feature p{font-size:15px;line-height:25px;color:var(--ink);margin-top:6px}
/* about */
.about-bg{position:absolute;left:0;top:1150px;width:1200px;height:1136px}
.about-title{position:absolute;left:101px;top:1418px;font-size:36px;font-weight:700}
.about-copy{position:absolute;left:101px;top:1476px;width:462px;font-size:14.5px;line-height:27.5px;color:var(--text)}
.video{position:absolute;left:600px;top:1388px;width:500px;height:337px;background:radial-gradient(circle at 80% 52%,#1e8f79 0 8%,#0e3a36 24%,#050806 56%),#050806}
.rule{position:absolute;left:101px;top:1810px;width:998px;height:1px;background:#cdd8e6}
/* testimonials */
.tm-title{top:1860px;font-size:38px;font-weight:700}
.person{position:absolute;top:1940px;width:240px;text-align:center}
.avatar{position:relative;width:134px;height:134px;border-radius:50%;margin:0 auto;background:linear-gradient(160deg,#c7d3e0,#5b7792)}
.badge{position:absolute;right:-6px;bottom:-2px;width:46px;height:46px;border-radius:50%;background:var(--white);display:flex;align-items:center;justify-content:center}
.badge span{width:38px;height:38px;border-radius:50%;background:linear-gradient(135deg,var(--teal),var(--blue));display:flex;align-items:center;justify-content:center;color:#fff;font-family:'Poppins',sans-serif;font-weight:700;font-size:26px;line-height:1;padding-top:10px}
.person h3{font-family:'Roboto',Arial,sans-serif;font-weight:400;font-size:22px;margin-top:16px}
.person p{font-size:13.3px;line-height:22px;color:var(--ink);margin-top:10px}
/* services */
.sv-title{top:2352px;font-size:38px;font-weight:700}
.sv-copy{position:absolute;left:180px;top:2414px;width:840px;text-align:center;font-size:14.3px;line-height:27.5px}
.card{position:absolute;top:2572px;width:316px;height:378px;background:var(--white);box-shadow:0 4px 22px rgba(20,40,80,.09)}
.card .art{position:absolute;left:60px;top:20px;width:196px;height:150px;border-radius:12px;background:linear-gradient(135deg,#bff2e0,#1aa989 55%,#0f6d6d)}
.card .line{position:absolute;left:20px;top:172px;width:276px;height:2px;background:linear-gradient(90deg,rgba(21,179,154,0),var(--teal),rgba(28,63,214,0))}
.card h3{position:absolute;left:0;top:196px;width:316px;text-align:center;font-size:22px;line-height:25px;font-weight:700}
.card ul{position:absolute;left:72px;list-style:none}
.card li{position:relative;padding-left:22px;font-size:15.5px;line-height:31.5px;color:var(--ink)}
.card li:before{content:"";position:absolute;left:0;top:10px;width:9px;height:9px;border-radius:50%;border:2px solid var(--sky);box-shadow:inset 0 0 0 2px #fff;background:var(--sky)}
/* footer */
.footer{position:absolute;left:0;top:3127px;width:1200px;height:349px;background:radial-gradient(ellipse at 70% 20%,#2a2a2a,var(--footer) 60%)}
.fcol{position:absolute;top:3190px}
.fcol h4{font-family:'Poppins',Arial,sans-serif;font-weight:600;font-size:17px;color:var(--white);margin-bottom:12px}
.fcol a{display:block;color:var(--white);font-size:14.5px;line-height:33px;text-decoration:none}
.social{position:absolute;top:3345px;width:17px;height:17px;border-radius:3px;background:var(--white)}
.email{position:absolute;left:808px;top:3231px;width:288px;height:47px;border-radius:24px;background:var(--white);font-size:14px;color:#555;display:flex;align-items:center;padding-left:24px}
.footer-rule{position:absolute;left:101px;top:3415px;width:998px;height:1px;background:#555}
.copyright{top:3438px;color:var(--white);font-size:14px}
</style>
</head>
<body>

<!-- HERO -->
<svg class="hero-bg" viewBox="0 0 1200 780" aria-hidden="true">
  <defs>
    <linearGradient id="heroFill" x1="0" y1="0" x2="1" y2="1">
      <stop offset="0" stop-color="#090c3c"/><stop offset="1" stop-color="#1a2aa8"/>
    </linearGradient>
  </defs>
  <polygon points="0,600 0,620 920,770 1200,690 1200,650" fill="#ececec"/>
  <path d="M0,0 H1200 V590 L960,742 Q930,756 900,748 L0,588 Z" fill="url(#heroFill)"/>
  <path d="M100,560 L170,535 Q195,528 215,540 L520,650 L470,672 Z" fill="#2f7df0"/>
  <path d="M960,742 L1200,600 V650 L1030,735 Q1000,745 975,742 Z" fill="#1fd39b"/>
</svg>

<div class="brand-mark brand" style="left:101px;top:26px;font-size:30px">
  <span class="dot" style="width:16px;height:16px"></span>LF
</div>
<nav class="nav">
  <a style="left:262px" href="#">ABOUT US</a>
  <a style="left:382px" href="#">OUR SERVICES</a>
  <a style="left:534px" href="#">TESTIMONIALS</a>
  <a style="left:690px" href="#">BLOG</a>
</nav>
<div class="flag" role="img" aria-label="English language"></div>
<a class="btn-outline" href="#">Schedule a Free Consultation</a>

<div class="hero-art" role="img" aria-label="Isometric illustration of glowing coin stacks on a circuit platform"></div>
<h1 class="hero-title">Your own cryptocurrency.<br>Secure, easy to use, and<br>built by an expert team.</h1>
<p class="hero-copy">Ledgerwise Forge adds professionalism to cryptocurrency development. Our done-for-you service covers everything from development and IT operations to ongoing support. You have access to a full team, for less than the typical cost of a single developer</p>
<a class="btn" href="#" style="left:101px;top:412px;width:155px;height:45px">Get Started</a>

<!-- WHY CHOOSE -->
<h2 class="center why-title">Why choose Ledgerwise Forge</h2>

<div class="feature" style="left:128px">
  <svg width="70" height="66" viewBox="0 0 70 66" fill="none" stroke="#1c3fd6" stroke-width="2.2">
    <circle cx="38" cy="20" r="16"/><circle cx="38" cy="20" r="10" stroke="#15b39a"/>
    <path d="M4 42 H14 V62 H4 Z M14 46 C26 40 34 40 42 46 H54 C58 46 58 52 54 52 H36 M14 58 C30 62 44 60 66 46 C68 42 62 40 58 44"/>
  </svg>
  <h3>Value</h3>
  <p>A team of experts, regular updates,<br>and fixed costs</p>
</div>
<div class="feature" style="left:450px">
  <svg width="72" height="66" viewBox="0 0 72 66" fill="none" stroke="#1c3fd6" stroke-width="2.2">
    <circle cx="30" cy="34" r="12"/><path d="M14 34 A16 16 0 0 1 46 34 M12 32 V42 M48 32 V42 M10 64 C12 52 20 48 30 48 C40 48 48 52 50 64"/>
    <rect x="44" y="4" width="24" height="16" rx="3" stroke="#15b39a"/><path d="M50 20 L48 26 L56 20"/>
  </svg>
  <h3>Support</h3>
  <p>Receive advice and other services,<br>beyond development.</p>
</div>
<div class="feature" style="left:771px">
  <svg width="74" height="66" viewBox="0 0 74 66" fill="none" stroke="#1c3fd6" stroke-width="2.2">
    <circle cx="37" cy="14" r="10" stroke="#15b39a"/><circle cx="37" cy="14" r="4"/>
    <circle cx="14" cy="34" r="6"/><circle cx="60" cy="34" r="6"/>
    <path d="M2 64 V50 C2 44 26 44 26 50 V64 M48 64 V50 C48 44 72 44 72 50 V64 M28 42 H46 V60 H28 Z"/>
  </svg>
  <h3>Commitment</h3>
  <p>Enjoy regular updates and<br>new features</p>
</div>

<!-- WHO WE ARE -->
<svg class="about-bg" viewBox="0 0 1200 1136" aria-hidden="true">
  <path d="M0,160 L880,6 Q920,0 960,14 L1200,120 V1136 H0 Z" fill="#e8f2fd"/>
  <path d="M75,182 L450,76 Q480,68 510,78 L545,92 L110,210 Z" fill="#c4dcfb"/>
  <path d="M990,26 Q1030,10 1070,30 L1200,90 V160 L990,40 Z" fill="#c3f1e2"/>
</svg>
<h2 class="about-title">Who We Are</h2>
<p class="about-copy">in addition to creating and enhancing cryptocurrencies for clients, the Ledgerwise Forge team has been running the Veltra cryptocurrency since 2017. We prefer long-term relationships, enabling us to deliver the very highest quality and giving you peace of mind that you've got a professional and trustworthy team at your side.</p>
<a class="btn" href="#" style="left:101px;top:1638px;width:155px;height:46px">Learn More</a>
<div class="video" role="img" aria-label="Video thumbnail showing a glowing digital coin over a trading chart">
  <svg class="abs" style="left:200px;top:118px" width="100" height="100" viewBox="0 0 100 100">
    <circle cx="50" cy="50" r="48" fill="rgba(255,255,255,.35)"/>
    <circle cx="50" cy="50" r="38" fill="#ffffff"/>
    <polygon points="42,38 64,50 42,62" fill="#1c6fd6"/>
  </svg>
</div>
<div class="rule"></div>

<!-- TESTIMONIALS -->
<h2 class="center tm-title">Testimonials</h2>
<svg class="abs" style="left:62px;top:2070px" width="20" height="38" viewBox="0 0 20 38"><path d="M18 2 L3 19 L18 36" fill="none" stroke="#222" stroke-width="1.8"/></svg>
<svg class="abs" style="left:1116px;top:2070px" width="20" height="38" viewBox="0 0 20 38"><path d="M2 2 L17 19 L2 36" fill="none" stroke="#222" stroke-width="1.8"/></svg>

<div class="person" style="left:95px">
  <div class="avatar" role="img" aria-label="Client portrait"><div class="badge"><span>&ldquo;</span></div></div>
  <h3>John Smith</h3>
  <p>"Lorem ipsum dolor sit amet, sectetur adipiscing elit, sed do eiusmod tempor incididunt ut labore et dolore"</p>
</div>
<div class="person" style="left:351px">
  <div class="avatar" role="img" aria-label="Client portrait" style="background:linear-gradient(160deg,#f2f2f2,#c9b8a8)"><div class="badge"><span>&ldquo;</span></div></div>
  <h3>John Smith</h3>
  <p>"Lorem ipsum dolor sit amet, sectetur adipiscing elit, sed do eiusmod tempor incididunt ut labore et dolore"</p>
</div>
<div class="person" style="left:608px">
  <div class="avatar" role="img" aria-label="Client portrait" style="background:linear-gradient(160deg,#5a5a5a,#2f4b4a)"><div class="badge"><span>&ldquo;</span></div></div>
  <h3>John Smith</h3>
  <p>"Lorem ipsum dolor sit amet, sectetur adipiscing elit, sed do eiusmod tempor incididunt ut labore et dolore"</p>
</div>
<div class="person" style="left:864px">
  <div class="avatar" role="img" aria-label="Client portrait" style="background:linear-gradient(160deg,#e6e6e6,#4d5f8a)"><div class="badge"><span>&ldquo;</span></div></div>
  <h3>John Smith</h3>
  <p>"Lorem ipsum dolor sit amet, sectetur adipiscing elit, sed do eiusmod tempor incididunt ut labore et dolore"</p>
</div>

<!-- SERVICES -->
<h2 class="center sv-title">Our Services</h2>
<p class="sv-copy">Ledgerwise Forge offers more than just development. We provide a complete solution and our clients receive access to expert advice, ongoing support, I.T. operations, mobile wallets, and even the creation of white papers, Our packages can be tailored to suit you to match your requirements or budget, you can simply pick and choose the features you would like. Alternatively, We can create a custom package just for you.</p>

<div class="card" style="left:100px">
  <div class="art" role="img" aria-label="Illustration of a team meeting around a table with charts"></div>
  <div class="line"></div>
  <h3>Blockchain creation<br>&amp; Launch</h3>
  <ul style="top:266px"><li>This is a list item</li><li>Another list item</li><li>Yup, another list item</li></ul>
</div>
<div class="card" style="left:442px">
  <div class="art" role="img" aria-label="Illustration of a developer working at a desk"></div>
  <div class="line"></div>
  <h3 style="top:208px">Basic</h3>
  <ul style="top:266px"><li>This is a list item</li><li>Another list item</li><li>Yup, another list item</li></ul>
</div>
<div class="card" style="left:784px">
  <div class="art" role="img" aria-label="Illustration of a small team collaborating at a table"></div>
  <div class="line"></div>
  <h3 style="top:208px">Mid-range</h3>
  <ul style="top:266px"><li>This is a list item</li><li>Another list item</li><li>Yup, another list item</li></ul>
</div>

<a class="btn" href="#" style="left:459px;top:2998px;width:282px;height:46px">Schedule a Free Consultation</a>

<!-- FOOTER -->
<footer class="footer"></footer>
<div class="brand-mark brand" style="left:101px;top:3230px;font-size:44px">
  <span class="dot" style="width:22px;height:22px"></span>LF
</div>
<span class="social" style="left:101px" role="img" aria-label="Social link"></span>
<span class="social" style="left:146px" role="img" aria-label="Social link"></span>
<span class="social" style="left:186px" role="img" aria-label="Social link"></span>
<span class="social" style="left:225px" role="img" aria-label="Social link"></span>

<div class="fcol" style="left:357px">
  <h4>Site Content</h4>
  <a href="#">Home</a><a href="#">About</a><a href="#">Feature</a><a href="#">Pricing</a><a href="#">Contact</a>
</div>
<div class="fcol" style="left:581px">
  <h4>Major Topics</h4>
  <a href="#">Search</a><a href="#">T&amp;Cs</a><a href="#">Privacy</a><a href="#">Commu</a>
</div>
<div class="fcol" style="left:808px">
  <h4>Get our Newsletter</h4>
</div>
<div class="email">Enter your email</div>
<a class="btn" href="#" style="left:808px;top:3291px;width:288px;height:47px;font-family:'Roboto',Arial,sans-serif;font-weight:500;font-size:16px">SUBSCRIBE</a>
<div class="footer-rule"></div>
<p class="center copyright">Copyright © 2021 Ledgerwise Forge. All rights reserved.</p>

</body>
</html>
```